Veltrane Industrial Coatings

We are looking to improve our business cards. Our company installs industrial floor and wall coatings in industrial, chemical and food processing plants.
Our coatings which consist of epoxy, urethane, and vinyl esters provide chemical and abrasion resistant surface with non-skid properties that are easy to clean.

Target Market(s)

food manufacturing, chemical plants, breweries and wineries, warehouses, clean room floors.

Industry/Entity Type

Construction

Contact Information for Business Card

improved current logo.

Colors

Designer to choose colors to be used in the design.

Requirements
Must have
• the information from uploaded file
Nice to have
• "We'll be outstanding on your floors."

```html
<!DOCTYPE html>
<html lang="en">
<head>
<meta charset="utf-8">
<title>Veltrane Industrial Coatings – Business Card</title>
<link href="https://fonts.googleapis.com/css2?family=Source+Sans+3:wght@400;600&family=Tinos&display=swap" rel="stylesheet">
<style>
  :root {
    --stage: #3f4150;
    --card-light-a: #dcdcdc;
    --card-light-b: #ffffff;
    --card-dark: #0d0002;
    --brand-blue: #3a4898;
    --ink: #1a1a1a;
    --ink-soft: #444444;
    --tagline-red: #5a1a10;
    --band-text: #f2f2f2;
    --logo-light: #cfcfcf;
  }
  * { margin: 0; padding: 0; box-sizing: border-box; }
  html, body { width: 1200px; height: 1176px; overflow: hidden; }
  body {
    background: var(--stage);
    font-family: "Source Sans 3", "Myriad Pro", sans-serif;
    position: relative;
  }
  .card {
    position: absolute;
    left: 280px;
    width: 617px;
    height: 352px;
    border-radius: 20px;
    overflow: hidden;
    box-shadow: 0 8px 18px rgba(0,0,0,0.35);
  }
  .card--front {
    top: 190px;
    background: linear-gradient(135deg, var(--card-light-a) 0%, var(--card-light-b) 65%);
  }
  .card--back {
    top: 590px;
    background: var(--card-dark);
  }

  .brand {
    position: absolute;
    display: flex;
    align-items: center;
  }
  .brand__mark {
    flex: none;
    background: var(--brand-blue);
    transform: rotate(45deg);
  }
  .brand__name {
    font-weight: 600;
    letter-spacing: 2px;
    line-height: 1;
  }
  .card--front .brand { right: 31px; top: 30px; gap: 16px; }
  .card--front .brand__mark { width: 38px; height: 38px; }
  .card--front .brand__name { font-size: 36px; color: var(--ink); }

  .card--back .brand { left: 50%; top: 150px; transform: translateX(-50%); gap: 30px; }
  .card--back .brand__mark { width: 62px; height: 62px; }
  .card--back .brand__name { font-size: 58px; color: var(--logo-light); }

  .person { position: absolute; left: 30px; top: 138px; }
  .person__name { font-size: 26px; color: var(--ink); font-weight: 400; line-height: 1.1; }
  .person__line {
    font-family: "Tinos", serif;
    font-size: 15px;
    color: var(--tagline-red);
    margin-top: 4px;
  }

  .divider {
    position: absolute;
    left: 30px; right: 31px; top: 206px;
    height: 1px;
    background: var(--brand-blue);
  }

  .contact-list, .address {
    position: absolute;
    top: 228px;
    list-style: none;
    font-size: 16px;
    color: var(--ink-soft);
    line-height: 26px;
  }
  .contact-list { left: 30px; }
  .contact-list li { display: flex; align-items: center; gap: 8px; }
  .contact-list svg { width: 15px; height: 15px; fill: var(--brand-blue); }
  .address { right: 57px; text-align: right; }
  .address__pin {
    position: absolute;
    right: -25px; top: 6px;
    width: 13px; height: 16px;
    fill: var(--brand-blue);
  }

  .web-band {
    position: absolute;
    left: 0; right: 0; bottom: 0;
    height: 28px;
    background: var(--brand-blue);
    color: var(--band-text);
    font-size: 15px;
    letter-spacing: 2px;
    text-align: center;
    line-height: 28px;
  }
  .web-back {
    position: absolute;
    left: 0; right: 0; top: 300px;
    text-align: center;
    color: var(--brand-blue);
    font-size: 13px;
    letter-spacing: 2.5px;
  }
</style>
</head>
<body>

<section class="card card--front" aria-label="Business card front">
  <div class="brand">
    <span class="brand__mark"></span>
    <span class="brand__name">VELTRANE</span>
  </div>

  <div class="person">
    <p class="person__name">Cal Brenner</p>
    <p class="person__line">1-800-555-0142</p>
  </div>

  <div class="divider"></div>

  <ul class="contact-list">
    <li>
      <svg viewBox="0 0 16 16" aria-hidden="true"><path d="M1 6c0-2 3-3.5 7-3.5S15 4 15 6v1.5h-3.5V6h-7v1.5H1z M3 8.5h10l1 5H2z"/></svg>
      (360) 555-0131
    </li>
    <li>
      <svg viewBox="0 0 16 16" aria-hidden="true"><path d="M4 1h7v4H4z M1 5h14v10H1z M3 7v6h2V7z M7 8h2v1.5H7z M10.5 8h2v1.5h-2z M7 11h2v1.5H7z M10.5 11h2v1.5h-2z" fill-rule="evenodd"/></svg>
      (360) 555-0133
    </li>
    <li>
      <svg viewBox="0 0 16 16" aria-hidden="true"><path d="M4.5 1h7v14h-7z M6 3v9h4V3z M7.3 13h1.4v1H7.3z" fill-rule="evenodd"/></svg>
      (360) 555-0177
    </li>
  </ul>

  <address class="address" style="font-style:normal">
    <svg class="address__pin" viewBox="0 0 12 16" aria-hidden="true"><path d="M6 0a6 6 0 0 1 6 6c0 4-6 10-6 10S0 10 0 6a6 6 0 0 1 6-6zm0 3.5a2.5 2.5 0 1 0 0 5 2.5 2.5 0 0 0 0-5z" fill-rule="evenodd"/></svg>
    Veltrane Inc.<br>
    PO Box 412<br>
    Marlow, WA 98602
  </address>

  <div class="web-band">www.veltranefloors.com</div>
</section>

<section class="card card--back" aria-label="Business card back">
  <div class="brand">
    <span class="brand__mark"></span>
    <span class="brand__name">VELTRANE</span>
  </div>
  <p class="web-back">www.veltranefloors.com</p>
</section>

</body>
</html>
```